International Development Cooperation Consultant needs a business card design

I need a business card design for myself as a way to present and introduce to wide range of organisations: international organisations, NGOs, governments, universities....
I am a consultant working in the field of governance, civil society and public sector. I carry out studies and provide advice for development agencies as well as think tanks on different topics such as civil society organisations in developing countries, corruption, climate change, monitoring and evaluation. I also provide technical assistance to governments in developing countries... These studies should help for example NGOs to play a better role in poor countries or where they are threatened, or improved the impact of aid in developing countries. Technical capacity should strengthen the organisation and empower the public civl servants in those countries. I would like to see designs that give a fresh, young, positive, alternative but at the same time serious impression. That reflects change, connecting people, the world, knowledge, multi-culturality... Most of people I have worked with say that 'I make things happen' !
Industry/Entity Type
Business
Contact Information for Business Card
Laia Corbera Vidal
International Development Consultant
Governance Expert
E-mail: laiacorbera@mailnest-example.com
Phone: +34655203817

```html
<!DOCTYPE html>
<html lang="en">
<head>
<meta charset="utf-8">
<title>Laia Corbera Vidal – Business Card</title>
<link rel="stylesheet" href="https://fonts.googleapis.com/css2?family=Exo+2:wght@400;500;600&display=swap">
<style>
  :root {
    --backdrop: #e9e6ec;
    --plum: #3e3447;
    --ink: #2f2838;
    --paper: #ffffff;
    --on-plum: #f4f1f7;
  }
  * { margin: 0; padding: 0; box-sizing: border-box; }
  html, body {
    width: 1200px; height: 900px; overflow: hidden;
    background: var(--backdrop);
    font-family: "Exo 2", sans-serif;
  }
  .canvas {
    width: 1200px; height: 900px;
    display: flex; flex-direction: column;
    align-items: center; justify-content: center; gap: 44px;
  }
  .card {
    width: 700px; height: 400px;
    border-radius: 16px;
    position: relative;
    box-shadow: 0 8px 24px rgba(40, 30, 50, 0.18);
  }
  .card--back {
    background: var(--plum);
    display: flex; align-items: center; justify-content: center;
  }
  .tagline {
    color: var(--on-plum);
    font-size: 17px; font-weight: 500;
    letter-spacing: 1.5px;
    text-transform: uppercase;
  }
  .card--front { background: var(--paper); color: var(--ink); }
  .identity {
    position: absolute; left: 150px; top: 110px; width: 470px;
    text-align: center;
  }
  .name {
    font-size: 23px; font-weight: 600; letter-spacing: 1px;
    text-transform: uppercase;
    padding-bottom: 12px;
  }
  .rule { height: 2px; background: var(--ink); }
  .roles {
    font-size: 19px; font-weight: 500; line-height: 1.15;
    padding: 10px 0 14px;
  }
  .contact { list-style: none; padding-top: 8px; }
  .contact__item {
    display: flex; align-items: center; justify-content: center; gap: 10px;
    font-size: 21px; font-weight: 500; line-height: 1.25;
  }
  .contact__icon { width: 22px; height: 22px; fill: var(--ink); flex: none; }
</style>
</head>
<body>
<main class="canvas">
  <section class="card card--back">
    <p class="tagline">I make things happen</p>
  </section>

  <section class="card card--front">
    <div class="identity">
      <h1 class="name">Laia Corbera Vidal</h1>
      <div class="rule"></div>
      <p class="roles">International Development Consultant<br>Governance Expert</p>
      <div class="rule"></div>
      <ul class="contact">
        <li class="contact__item">
          <svg class="contact__icon" viewBox="0 0 24 24" aria-hidden="true">
            <path d="M2 9l10-6 10 6v11H2z"/>
            <path d="M4 10l8 5 8-5" fill="none" stroke="#fff" stroke-width="1.6"/>
          </svg>
          laiacorbera@mailnest-example.com
        </li>
        <li class="contact__item">
          <svg class="contact__icon" viewBox="0 0 24 24" aria-hidden="true">
            <path d="M6.6 10.8a15 15 0 006.6 6.6l2.2-2.2c.3-.3.7-.4 1-.2 1.1.4 2.3.6 3.6.6.6 0 1 .4 1 1V20c0 .6-.4 1-1 1A17 17 0 013 4c0-.6.4-1 1-1h3.5c.6 0 1 .4 1 1 0 1.3.2 2.5.6 3.6.1.3 0 .7-.2 1z"/>
          </svg>
          +34655203817
        </li>
      </ul>
    </div>
  </section>
</main>
</body>
</html>
```